Kestrel Ink BC 2019

Hi!
As seen from the attached, I created a 2018 BC that I really like.
It features company details on one side, and a calendar on the other side. The BC is 7" x 2" with a score, so folded it's a regular sized BC.
Company details remain the same, but I need to upgrade and refresh the calendar to 2019. Let your creative juices flow!

The submitted designs so far, while not terrible, most don't take into account that I need a refresher on the current design, but it's a BC that is double sided, and the size of a BC that's side by side wide, with score. (see the attached BC 2018 design). I need the BC to be updated with a 2019 calendar, but essentially because it's such a tiny size, to work the realistic space allocated, and make it readable and striking to stand out and very usable/practical. Let's do this people!

```html
<!DOCTYPE html>
<html lang="en">
<head>
<meta charset="utf-8">
<title>Kestrel Ink – 2019 Calendar Business Card</title>
<link href="https://fonts.googleapis.com/css2?family=Open+Sans:wght@400;600&family=Oswald:wght@400;500;700&family=Roboto+Condensed:wght@400&family=Caveat:wght@400&display=swap" rel="stylesheet">
<style>
:root{
  --backdrop:#a5a6a8;
  --paper:#ffffff;
  --ink:#111111;
  --band:#000000;
  --cyan:#29abe2;
  --magenta:#ec008c;
  --yellow:#f5e31a;
  --ghost:#e7e7e7;
  --rule:#555555;
}
*{margin:0;padding:0;box-sizing:border-box}
html,body{width:1200px;height:1200px;overflow:hidden;background:var(--backdrop)}
.canvas{position:relative;width:1200px;height:1200px}

/* ---------- Front: company details ---------- */
.card-front{position:absolute;left:30px;top:188px;width:1140px;height:326px;background:var(--paper)}
.contact{position:absolute;left:40px;font-family:"Open Sans",sans-serif;font-size:22px;color:var(--ink);display:flex;align-items:center}
.contact-item{display:flex;align-items:center;gap:6px;margin-right:22px}
.contact-item svg{width:20px;height:20px;fill:var(--ink)}
.contact-phones{top:113px}
.contact-web{top:167px}
.contact-web .contact-item:first-child{margin-right:50px}
.contact-rule{position:absolute;left:41px;top:154px;width:495px;height:1px;background:var(--ink)}
.brand{position:absolute;left:785px;top:115px;display:flex;align-items:center;gap:12px}
.brand-mark{width:22px;height:22px;background:var(--magenta)}
.brand-name{font-family:"Open Sans",sans-serif;font-weight:400;font-size:44px;color:var(--ink);letter-spacing:.5px}
.band{position:absolute;left:0;top:274px;width:100%;height:52px;background:var(--band);display:flex;align-items:center}
.taglines{margin-left:23px;font-family:"Roboto Condensed",sans-serif;font-size:14px;display:flex;align-items:center;white-space:nowrap}
.taglines .dot{margin:0 14px;font-size:10px}
.t-cyan{color:var(--cyan)}.t-magenta{color:var(--magenta)}.t-yellow{color:var(--yellow)}
.motto{position:absolute;left:718px;font-family:"Caveat",cursive;font-size:22px;color:#fff;letter-spacing:.4px;white-space:nowrap}

/* ---------- Back: 2019 calendar ---------- */
.card-back{position:absolute;left:30px;top:600px;width:1141px;height:326px;background:var(--paper);overflow:hidden}
.year{position:absolute;left:362px;top:57px;font-family:"Oswald",sans-serif;font-weight:700;font-size:250px;line-height:1;color:var(--ghost);letter-spacing:-10px;transform:scaleX(.85);transform-origin:left top}
.month{position:absolute;width:165px;font-family:"Oswald",sans-serif}
.month h3{text-align:center;font-weight:500;font-size:18px;letter-spacing:1px;line-height:1;margin-bottom:9px;color:var(--accent)}
.days{display:grid;grid-template-columns:repeat(7,1fr);text-align:center;font-size:11px;font-weight:500;color:var(--ink);line-height:16px}
.days i{font-style:normal}
.days i:nth-child(-n+7){border-bottom:1px solid var(--rule);padding-bottom:3px;margin-bottom:4px;font-size:12px;font-weight:400}
.days i:nth-child(7n+1){color:var(--accent)}
.m-cyan{--accent:var(--cyan)}
.m-magenta{--accent:var(--magenta)}
.m-yellow{--accent:var(--yellow)}
.row-1{top:18px}.row-2{top:178px}
.col-1{left:25px}.col-2{left:210px}.col-3{left:398px}.col-4{left:586px}.col-5{left:775px}.col-6{left:962px}
.days i.marked{position:relative}
.days i.marked::after{content:"";position:absolute;left:50%;top:50%;width:17px;height:17px;margin:-9px 0 0 -9px;border:2px solid var(--magenta);border-radius:50%}
.day-note{position:absolute;left:818px;top:304px;font-family:"Caveat",cursive;font-size:10px;color:var(--magenta);white-space:nowrap}
</style>
</head>
<body>
<div class="canvas">

  <section class="card-front">
    <div class="contact contact-phones">
      <span class="contact-item"><svg viewBox="0 0 24 24"><path d="M6.6 10.8a15.1 15.1 0 0 0 6.6 6.6l2.2-2.2a1 1 0 0 1 1-.25 11.4 11.4 0 0 0 3.6.57 1 1 0 0 1 1 1V20a1 1 0 0 1-1 1A17 17 0 0 1 3 4a1 1 0 0 1 1-1h3.5a1 1 0 0 1 1 1c0 1.250.2 2.45.57 3.57a1 1 0 0 1-.25 1z"/></svg>555.210.4410</span>
      <span class="contact-item"><svg viewBox="0 0 24 24"><path d="M8 1h8a2 2 0 0 1 2 2v18a2 2 0 0 1-2 2H8a2 2 0 0 1-2-2V3a2 2 0 0 1 2-2zm0 3v14h8V4zm4 15.5a1 1 0 1 0 0 2 1 1 0 0 0 0-2z"/></svg>555.382.6095</span>
      <span class="contact-item"><svg viewBox="0 0 24 24"><path d="M7 2h8l3 3v4H7zM3 10h18a1 1 0 0 1 1 1v9a1 1 0 0 1-1 1H3a1 1 0 0 1-1-1v-9a1 1 0 0 1 1-1zm3 3v2h12v-2zm0 4v2h3v-2zm5 0v2h3v-2zm5 0v2h2v-2z"/></svg>555.210.4411</span>
    </div>
    <div class="contact-rule"></div>
    <div class="contact contact-web">
      <span class="contact-item"><svg viewBox="0 0 24 24"><path d="M2 5h20v14H2zm2 2v.4l8 5.6 8-5.6V7zm0 2.8V17h16V9.8l-8 5.6z"/></svg>pickup@kestrelink.com</span>
      <span class="contact-item"><svg viewBox="0 0 24 24"><path d="M3 3h18v13H3zm2 2v9h14V5zM1 18h22v2H1z"/></svg>kestrelink.com</span>
    </div>
    <div class="brand">
      <span class="brand-mark"></span>
      <span class="brand-name">Kestrel Ink</span>
    </div>
    <div class="band">
      <p class="taglines">
        <span class="t-cyan">Print with a lighter footprint</span><span class="dot t-yellow">•</span>
        <span class="t-magenta">Leave the planet greener</span><span class="dot t-cyan">•</span>
        <span class="t-yellow">Share good work with neighbors</span>
      </p>
      <p class="motto">Every cartridge gets a second run</p>
    </div>
  </section>

  <section class="card-back">
    <div class="year">2019</div>

    <div class="month m-cyan row-1 col-1"><h3>JANUARY</h3><div class="days"><i>S</i><i>M</i><i>T</i><i>W</i><i>T</i><i>F</i><i>S</i><i></i><i></i><i>1</i><i>2</i><i>3</i><i>4</i><i>5</i><i>6</i><i>7</i><i>8</i><i>9</i><i>10</i><i>11</i><i>12</i><i>13</i><i>14</i><i>15</i><i>16</i><i>17</i><i>18</i><i>19</i><i>20</i><i>21</i><i>22</i><i>23</i><i>24</i><i>25</i><i>26</i><i>27</i><i>28</i><i>29</i><i>30</i><i>31</i></div></div>

    <div class="month m-magenta row-1 col-2"><h3>FEBRUARY</h3><div class="days"><i>S</i><i>M</i><i>T</i><i>W</i><i>T</i><i>F</i><i>S</i><i></i><i></i><i></i><i></i><i></i><i>1</i><i>2</i><i>3</i><i>4</i><i>5</i><i>6</i><i>7</i><i>8</i><i>9</i><i>10</i><i>11</i><i>12</i><i>13</i><i>14</i><i>15</i><i>16</i><i>17</i><i>18</i><i>19</i><i>20</i><i>21</i><i>22</i><i>23</i><i>24</i><i>25</i><i>26</i><i>27</i><i>28</i></div></div>

    <div class="month m-yellow row-1 col-3"><h3>MARCH</h3><div class="days"><i>S</i><i>M</i><i>T</i><i>W</i><i>T</i><i>F</i><i>S</i><i></i><i></i><i></i><i></i><i></i><i>1</i><i>2</i><i>3</i><i>4</i><i>5</i><i>6</i><i>7</i><i>8</i><i>9</i><i>10</i><i>11</i><i>12</i><i>13</i><i>14</i><i>15</i><i>16</i><i>17</i><i>18</i><i>19</i><i>20</i><i>21</i><i>22</i><i>23</i><i>24</i><i>25</i><i>26</i><i>27</i><i>28</i><i>29</i><i>30</i><i>31</i></div></div>

    <div class="month m-cyan row-1 col-4"><h3>APRIL</h3><div class="days"><i>S</i><i>M</i><i>T</i><i>W</i><i>T</i><i>F</i><i>S</i><i></i><i>1</i><i>2</i><i>3</i><i>4</i><i>5</i><i>6</i><i>7</i><i>8</i><i>9</i><i>10</i><i>11</i><i>12</i><i>13</i><i>14</i><i>15</i><i>16</i><i>17</i><i>18</i><i>19</i><i>20</i><i>21</i><i>22</i><i>23</i><i>24</i><i>25</i><i>26</i><i>27</i><i>28</i><i>29</i><i>30</i></div></div>

    <div class="month m-magenta row-1 col-5"><h3>MAY</h3><div class="days"><i>S</i><i>M</i><i>T</i><i>W</i><i>T</i><i>F</i><i>S</i><i></i><i></i><i></i><i>1</i><i>2</i><i>3</i><i>4</i><i>5</i><i>6</i><i>7</i><i>8</i><i>9</i><i>10</i><i>11</i><i>12</i><i>13</i><i>14</i><i>15</i><i>16</i><i>17</i><i>18</i><i>19</i><i>20</i><i>21</i><i>22</i><i>23</i><i>24</i><i>25</i><i>26</i><i>27</i><i>28</i><i>29</i><i>30</i><i>31</i></div></div>

    <div class="month m-yellow row-1 col-6"><h3>JUNE</h3><div class="days"><i>S</i><i>M</i><i>T</i><i>W</i><i>T</i><i>F</i><i>S</i><i></i><i></i><i></i><i></i><i></i><i></i><i>1</i><i>2</i><i>3</i><i>4</i><i>5</i><i>6</i><i>7</i><i>8</i><i>9</i><i>10</i><i>11</i><i>12</i><i>13</i><i>14</i><i>15</i><i>16</i><i>17</i><i>18</i><i>19</i><i>20</i><i>21</i><i>22</i><i>23</i><i>24</i><i>25</i><i>26</i><i>27</i><i>28</i><i>29</i><i>30</i></div></div>

    <div class="month m-magenta row-2 col-1"><h3>JULY</h3><div class="days"><i>S</i><i>M</i><i>T</i><i>W</i><i>T</i><i>F</i><i>S</i><i></i><i>1</i><i>2</i><i>3</i><i>4</i><i>5</i><i>6</i><i>7</i><i>8</i><i>9</i><i>10</i><i>11</i><i>12</i><i>13</i><i>14</i><i>15</i><i>16</i><i>17</i><i>18</i><i>19</i><i>20</i><i>21</i><i>22</i><i>23</i><i>24</i><i>25</i><i>26</i><i>27</i><i>28</i><i>29</i><i>30</i><i>31</i></div></div>

    <div class="month m-yellow row-2 col-2"><h3>AUGUST</h3><div class="days"><i>S</i><i>M</i><i>T</i><i>W</i><i>T</i><i>F</i><i>S</i><i></i><i></i><i></i><i></i><i>1</i><i>2</i><i>3</i><i>4</i><i>5</i><i>6</i><i>7</i><i>8</i><i>9</i><i>10</i><i>11</i><i>12</i><i>13</i><i>14</i><i>15</i><i>16</i><i>17</i><i>18</i><i>19</i><i>20</i><i>21</i><i>22</i><i>23</i><i>24</i><i>25</i><i>26</i><i>27</i><i>28</i><i>29</i><i>30</i><i>31</i></div></div>

    <div class="month m-cyan row-2 col-3"><h3>SEPTEMBER</h3><div class="days"><i>S</i><i>M</i><i>T</i><i>W</i><i>T</i><i>F</i><i>S</i><i>1</i><i>2</i><i>3</i><i>4</i><i>5</i><i>6</i><i>7</i><i>8</i><i>9</i><i>10</i><i>11</i><i>12</i><i>13</i><i>14</i><i>15</i><i>16</i><i>17</i><i>18</i><i>19</i><i>20</i><i>21</i><i>22</i><i>23</i><i>24</i><i>25</i><i>26</i><i>27</i><i>28</i><i>29</i><i>30</i></div></div>

    <div class="month m-magenta row-2 col-4"><h3>OCTOBER</h3><div class="days"><i>S</i><i>M</i><i>T</i><i>W</i><i>T</i><i>F</i><i>S</i><i></i><i></i><i>1</i><i>2</i><i>3</i><i>4</i><i>5</i><i>6</i><i>7</i><i>8</i><i>9</i><i>10</i><i>11</i><i>12</i><i>13</i><i>14</i><i>15</i><i>16</i><i>17</i><i>18</i><i>19</i><i>20</i><i>21</i><i>22</i><i>23</i><i>24</i><i>25</i><i>26</i><i>27</i><i>28</i><i>29</i><i>30</i><i>31</i></div></div>

    <div class="month m-yellow row-2 col-5"><h3>NOVEMBER</h3><div class="days"><i>S</i><i>M</i><i>T</i><i>W</i><i>T</i><i>F</i><i>S</i><i></i><i></i><i></i><i></i><i></i><i>1</i><i>2</i><i>3</i><i>4</i><i>5</i><i>6</i><i>7</i><i>8</i><i>9</i><i>10</i><i>11</i><i>12</i><i>13</i><i>14</i><i class="marked">15</i><i>16</i><i>17</i><i>18</i><i>19</i><i>20</i><i>21</i><i>22</i><i>23</i><i>24</i><i>25</i><i>26</i><i>27</i><i>28</i><i>29</i><i>30</i></div></div>

    <div class="month m-cyan row-2 col-6"><h3>DECEMBER</h3><div class="days"><i>S</i><i>M</i><i>T</i><i>W</i><i>T</i><i>F</i><i>S</i><i>1</i><i>2</i><i>3</i><i>4</i><i>5</i><i>6</i><i>7</i><i>8</i><i>9</i><i>10</i><i>11</i><i>12</i><i>13</i><i>14</i><i>15</i><i>16</i><i>17</i><i>18</i><i>19</i><i>20</i><i>21</i><i>22</i><i>23</i><i>24</i><i>25</i><i>26</i><i>27</i><i>28</i><i>29</i><i>30</i><i>31</i></div></div>

    <p class="day-note">*America Recycles Day</p>
  </section>

</div>
</body>
</html>
```